Leadership Seminar Concept

We want the theme picture/design of the Leadership Seminar Flyer with theme "Inspiring Commitment"

Industry/Entity Type

Leadership

```html
<!DOCTYPE html>
<html lang="en">
<head>
<meta charset="utf-8">
<title>Inspiring Commitment — Leadership Seminar Flyer</title>
<link rel="stylesheet" href="https://fonts.googleapis.com/css2?family=Raleway:ital,wght@0,400;0,700;0,800;0,900;1,700&display=swap">
<style>
  :root {
    --page-bg: #e9ecef;
    --sky-top: #4a93d2;
    --sky-mid: #5fabe2;
    --sky-low: #9fcdf0;
    --sky-white: #ffffff;
    --navy: #003b71;
    --text-navy: #0d3a66;
    --white: #ffffff;
  }
  * { margin: 0; padding: 0; box-sizing: border-box; }
  html, body {
    width: 1200px;
    height: 1200px;
    overflow: hidden;
    background: var(--page-bg);
  }
  .flyer {
    position: absolute;
    left: 136px;
    top: 0;
    width: 928px;
    height: 1200px;
    overflow: hidden;
    font-family: "Raleway", sans-serif;
  }
  .flyer__sky {
    position: absolute;
    inset: 0;
    background:
      radial-gradient(ellipse 70% 45% at 85% 100%, var(--sky-white) 0%, rgba(255,255,255,0.85) 35%, rgba(255,255,255,0) 75%),
      linear-gradient(180deg, var(--sky-top) 0%, var(--sky-mid) 45%, var(--sky-low) 85%, #d9ecfa 100%);
  }
  .flyer__content {
    position: absolute;
    left: 70px;
    top: 140px;
    width: 790px;
  }
  .headline {
    line-height: 1;
    font-weight: 900;
    text-transform: uppercase;
  }
  .headline__top {
    display: block;
    font-size: 162px;
    color: var(--navy);
    letter-spacing: -3px;
    line-height: 0.86;
  }
  .headline__bottom {
    display: block;
    font-size: 110px;
    color: var(--white);
    letter-spacing: -1px;
    line-height: 0.9;
    margin-top: 4px;
  }
  .subtitle {
    margin-top: 20px;
    font-size: 32px;
    font-weight: 800;
    color: var(--navy);
    line-height: 38px;
    letter-spacing: -0.8px;
  }
  .body-copy {
    margin-top: 20px;
    font-size: 19px;
    line-height: 29.5px;
    color: var(--text-navy);
    text-align: justify;
    letter-spacing: -0.3px;
  }
  .body-copy + .body-copy { margin-top: 16px; }
  .body-copy strong { font-weight: 700; }
  .invitation {
    margin-top: 18px;
    width: 590px;
    font-size: 30px;
    line-height: 39px;
    font-weight: 700;
    font-style: italic;
    color: var(--white);
    letter-spacing: -0.5px;
  }
  .flyer__art {
    position: absolute;
    left: 0;
    top: 780px;
    width: 890px;
    height: 360px;
    background: radial-gradient(ellipse 60% 50% at 55% 55%, rgba(140,190,230,0.35), rgba(140,190,230,0));
  }
</style>
</head>
<body>
  <main class="flyer">
    <div class="flyer__sky" role="img" aria-label="Bright blue sky fading to white clouds"></div>
    <div class="flyer__art" role="img" aria-label="Broken chain whose last links turn into birds flying upward"></div>
    <section class="flyer__content">
      <h1 class="headline">
        <span class="headline__top">Inspiring</span>
        <span class="headline__bottom">Commitment</span>
      </h1>
      <p class="subtitle">Shifting self, your people and your organization<br>from static to movement to momentum</p>
      <p class="body-copy"><strong>Inspiring commitment is enabling others to act.</strong> It involves energizing individuals to strive towards a compelling vision of the future, guiding people through change, keeping everyone aligned, building trust and open channels of communication, while reinforcing success.</p>
      <p class="body-copy"><strong>Shiftability is responding to outward demands from inward strength, purpose and skill.</strong> The mindset of shiftability acknowledges the need for change and embraces it, keeping an open mind about new ideas while wisely retaining things that still apply- always learning, always building, always growing.</p>
      <p class="invitation">We invite you to a journey of greatness where you’ll learn and practice tools for thriving as a leader by inspiring momentum.</p>
    </section>
  </main>
</body>
</html>
```